Wordpress Design for Financial Trading Software

Our Software QuantoMesh allows clients to program their trading strategy and use it to trade automatically on stock markets. For further details please visit our preliminary / draft web page: http://www.quantomesh-example.ch/wordpress.
We would like the Web Page to represent the following values:
- Innovative
- High Tech
- High Quality
- Professional
- Sophisticated
- State-of-the-art
- Modern
- Versatile
We need a Design based on a PSD file for the Main Page containing the following:
Header:
- Logo + optional Image / Graphic / Slogan / Quote
- Menu Bar with drop-down for Sub-Menus
- Search Box
Full Width Featured Content Area
- Main Description of the Product (with read-more Link + optional Image / Graphic)
Smaller Featured Content Areas:
- Product Features (with read-more Link + optional Icon)
- Documentation and Demo (with read-more Link + optional Icon)
- Professional Services (with read-more Link + optional Icon)
- Training (with read-more Link + optional Icon)
Latest News:
- 3-5 latest News + option Image / Grafic
Testimonial:
- 1 Customer Testimonial with Photo
Footer:
- Copyright and "all rights reserved" Notice
- Privacy Policy
- Contact Info: Address, Phone Number and Email
- Link to Site-Map
- Social Media Connectors (Chatterwall, CareerWeave, RSS Feed & Email)
Guidelines for Style/Theme:
- Well structured, Lean, Easy-to-use Page
- Use of existing Logo
- Sans-Serif Fonts
- Colors matching our Logo (not too many Colors)
- Main Focus: Desktop-Computers.
- However: Page should be readable on mobile Devices also
- Please show one element of the navigation bar in selected state with drop-down
- After the contest we will work with the Designer on the other Pages
- We will need a PSD File, so that we can organize the actual coding of the Wordpress Page / Theme
- If images / photos are used, they have to be royalty-free.
Example Pages that we like:
http://www.brindlecove.example/
http://www.hqz.example/
http://www.mockturn.example/
http://www.marketloft.example/
http://www.nimbravault.example/
http://www.shelfgrid.example/
http://www.pme-werkplatz.example.ch/
https://www.o-volving.example/
http://www.dealharbor.example/
https://sketchrally.example/web-design/contests/green-power-ventures-exchange-portal-website-design-402817/entries/38172640
https://sketchrally.example/web-design/contests/website-design-wanted-halvex-holdings-57210/entries/6431872
http://files.artpooling.example/design_img/482917/37650/37650_2948301_482917_image.jpg
WordPress Plugins currently in use:
- Quick Safe Inquiry Box
- Glowpane Album
- PinTrail Simple Terrain Charts
Reason: A few Designers let us know, that they need more time to work on their Designs. We are in no rush and would like to see as many good Designs as possible!
Target Market(s)
Investment Banks and Hedge Funds
Industry/Entity Type
Trade

```html
<!DOCTYPE html>
<html lang="en">
<head>
<meta charset="utf-8">
<title>QuantoMesh – Algorithmic Trading Platform</title>
<link rel="stylesheet" href="https://fonts.googleapis.com/css2?family=Roboto+Condensed:wght@300;400;700&family=Arimo:wght@400;700&display=swap">
<style>
:root{
  --gold:#c8a84f;
  --gold-soft:#e6d6a0;
  --ink:#333a40;
  --text:#4a4a4a;
  --muted:#9a9a9a;
  --slate-dark:#4f5963;
  --line:#e2e2e2;
  --footer:#2c3137;
  --footer-line:#3a4047;
  --footer-text:#aab0b6;
  --white:#ffffff;
}
*{margin:0;padding:0;box-sizing:border-box}
html,body{width:1200px;height:2254px;overflow:hidden;background:var(--white)}
body{position:relative;font-family:"Arimo",Arial,sans-serif;color:var(--text);font-size:14px}
.abs{position:absolute}
.head{font-family:"Roboto Condensed",Arial Narrow,sans-serif;font-weight:700;color:var(--ink);text-transform:uppercase}
.btn{position:absolute;display:flex;align-items:center;justify-content:center;font-family:"Roboto Condensed",sans-serif;font-size:13px;text-transform:uppercase;border-radius:5px}
.btn-slate{background:linear-gradient(#8994a0,#5f6a75);color:var(--white);border:2px solid #c9ced3}
.btn-gold{background:linear-gradient(#e7d394,#c9ab58);color:var(--ink);border:2px solid #d8cfb0}
.btn-small{font-size:11px;border-radius:4px}

/* header */
.search{left:957px;top:12px;width:218px;height:46px;background:#f1efe6;border-radius:6px;font-family:"Roboto Condensed",sans-serif;font-size:15px;color:var(--ink);padding:14px 14px}
.search svg{position:absolute;right:14px;top:10px}
.logo{left:52px;top:74px;display:flex;align-items:center;gap:12px;font-family:"Roboto Condensed",sans-serif;font-weight:700;font-size:40px;color:var(--slate-dark)}
.logo i{display:block;width:26px;height:26px;background:var(--gold)}
.nav{left:640px;top:98px;width:560px;height:30px;font-family:"Roboto Condensed",sans-serif;font-size:14px;color:var(--ink);text-transform:uppercase}
.nav span{position:absolute;top:4px;transform:translateX(-50%);white-space:nowrap}
.nav .active{background:var(--gold-soft);border-radius:4px;padding:5px 16px;top:-6px}
.dropdown{left:817px;top:141px;width:175px;z-index:20}
.dropdown div{height:40px;margin-bottom:5px;background:linear-gradient(#5b656f,#464f58);color:var(--white);font-family:"Roboto Condensed",sans-serif;font-size:14px;padding:0 22px;display:flex;align-items:center;box-shadow:0 2px 4px rgba(0,0,0,.3)}
.dropdown div.on{background:var(--gold-soft);color:var(--ink)}
.rule{left:0;width:1200px;height:2px;background:var(--line)}

/* hero */
.hero-title{left:35px;top:250px;font-size:23px}
.hero-copy{left:35px;top:304px;width:410px;font-size:13.5px;line-height:23px;color:var(--ink)}
.hero-shot{left:503px;top:225px;width:677px;height:357px;background:linear-gradient(160deg,#2b3a4c,#0f1620 60%,#1d2a38)}
.dots{left:518px;top:630px;display:flex;gap:8px}
.dots i{width:13px;height:13px;border-radius:50%;background:#c7cbcf;display:block}
.dots i.on{background:var(--slate-dark)}

/* intro */
.intro{left:0;top:694px;width:1200px;text-align:center;font-family:"Roboto Condensed",sans-serif;font-weight:300;font-size:29px;line-height:35px;color:#555}
.intro b{color:var(--gold);font-weight:700}

/* features */
.feature{top:800px;width:220px;text-align:center}
.feature .icon{width:82px;height:82px;border-radius:50%;margin:0 auto;display:flex;align-items:center;justify-content:center;background:linear-gradient(#8a96a2,#5d6873);border:4px solid #e3e6e9}
.feature .icon.gold{background:linear-gradient(#e0c575,#b4953f)}
.feature h3{margin-top:22px;height:48px;font-size:16px;line-height:20px}
.feature p{font-size:13.5px;line-height:20px;text-align:left;color:var(--ink)}
.feature .btn{position:relative;margin:20px auto 0;width:80px;height:26px}

/* about tabs */
.sec-title{font-size:19px}
.tabs{left:10px;top:1213px;width:641px;height:38px;font-family:"Roboto Condensed",sans-serif;font-size:14px;text-transform:uppercase;z-index:2}
.tabs span{position:absolute;top:11px;color:var(--gold)}
.tabs .current{top:0;left:0;height:38px;padding:11px 22px;border:2px solid var(--line);border-bottom:none;background:var(--white);color:var(--ink)}
.panel{left:10px;top:1249px;width:641px;height:290px;border:2px solid var(--line);border-radius:0 6px 6px 6px}
.product-box{left:25px;top:1294px;width:137px;height:200px;background:linear-gradient(135deg,#4a4f55,#111417 70%)}
.panel-copy{left:198px;top:1306px;width:432px;font-size:13px;line-height:18px;text-align:justify;color:var(--ink)}

/* news */
.news{left:759px;width:420px;height:90px}
.news .thumb{position:absolute;left:0;top:0;width:94px;height:54px;border:2px solid #ddd}
.news p{position:absolute;left:123px;top:-2px;width:295px;font-size:13.5px;line-height:22px;color:var(--muted)}
.news em{position:absolute;right:4px;top:66px;font-size:14px;color:var(--ink)}

/* testimonials */
.testi-head{left:0;top:1570px;width:1200px;text-align:center}
.testi-head h2{display:inline-block;background:var(--white);padding:0 14px;font-size:19px}
.testi-head p{font-size:14px;color:var(--gold);margin-top:2px}
.person{top:1658px;width:240px;text-align:center}
.person .photo{width:116px;height:116px;border-radius:50%;margin:0 auto;border:4px solid #eee;background:linear-gradient(#d9dde1,#8d969e)}
.person h4{margin-top:18px;font-size:11.5px;color:var(--ink)}
.person p{margin:16px auto 0;width:218px;font-size:13.5px;line-height:21px;text-align:left;color:var(--ink)}
.arrow{top:1768px}

/* footer */
.footer{left:0;top:1939px;width:1200px;height:315px;background:var(--footer)}
.f-col-line{top:1990px;width:1px;height:230px;background:var(--footer-line)}
.f-title{font-family:"Roboto Condensed",sans-serif;font-weight:700;font-size:14px;color:var(--gold);text-transform:uppercase;top:1966px}
.f-links{left:10px;top:2020px;font-size:12px;line-height:23px;color:var(--footer-text);text-transform:uppercase}
.f-copy{left:10px;top:2188px;font-size:12px;color:var(--gold)}
.social{left:460px;display:flex;align-items:center;gap:16px;font-family:"Roboto Condensed",sans-serif;font-weight:700;font-size:15px;color:var(--footer-text)}
.social i{display:block;width:28px;height:28px;border-radius:50%;background:#6a737c}
.newsletter{left:460px;top:2166px;font-size:12.5px;color:var(--footer-text)}
.email{left:458px;top:2199px;width:262px;height:42px;background:var(--white);border-radius:6px;border:3px solid #d0d3d6;font-family:"Roboto Condensed",sans-serif;font-size:13px;color:#888;padding:10px 0 0 38px}
.email b{position:absolute;right:4px;top:4px;width:48px;height:28px;background:var(--footer);color:var(--white);border-radius:4px;font-weight:400;display:flex;align-items:center;justify-content:center}
.f-logo{left:957px;top:2044px;display:flex;align-items:center;gap:10px;font-family:"Roboto Condensed",sans-serif;font-weight:700;font-size:30px;color:var(--footer-text)}
.f-logo i{display:block;width:20px;height:20px;background:var(--gold)}
.f-address{left:957px;top:2120px;font-size:13px;line-height:27px;color:var(--footer-text)}
</style>
</head>
<body>

<div class="abs rule" style="top:156px"></div>

<section>
  <h1 class="abs head hero-title">QuantoMesh Software</h1>
  <p class="abs hero-copy">Lorem Ipsum is simply dummy text of the printing and typesetting industry. Lorem Ipsum has been the industry's standard dummy text ever since the 1500s, when an unknown printer took a galley of type and scrambled it to make a type specimen book. It has survived not only five centuries, but also the leap into electronic typesetting, remaining essentially unchanged. It was popularised in the 1960s with the release of Typeleaf sheets containing Lorem</p>
  <div class="btn btn-slate" style="left:31px;top:493px;width:115px;height:44px">Read More</div>
  <div class="btn btn-gold" style="left:158px;top:493px;width:114px;height:44px">Get Demo</div>
  <div class="abs hero-shot" role="img" aria-label="Screenshot of the trading platform dashboard with strategy tables and a green bar chart"></div>
  <div class="abs dots"><i></i><i></i><i></i><i class="on"></i></div>
</section>

<header>
  <div class="abs search">Search Keywords
    <svg width="26" height="26" viewBox="0 0 26 26"><circle cx="10" cy="10" r="7" fill="none" stroke="#333a40" stroke-width="3"/><line x1="15" y1="15" x2="23" y2="23" stroke="#333a40" stroke-width="4" stroke-linecap="round"/></svg>
  </div>
  <div class="abs logo"><i></i>QuantoMesh</div>
  <nav class="abs nav">
    <span style="left:46px">Home</span>
    <span style="left:130px">About Us</span>
    <span class="active" style="left:221px">Services</span>
    <span style="left:317px">Portfolio</span>
    <span style="left:398px">Blog</span>
    <span style="left:486px">Contact Us</span>
  </nav>
  <div class="abs dropdown">
    <div>Services</div><div>Services</div><div>Services</div><div class="on">Services</div>
  </div>
</header>

<div class="abs rule" style="top:657px"></div>

<p class="abs intro">Hello ! We are &nbsp;<b>QUANTOMESH</b>&nbsp; This is a &nbsp;BUSSINESS IT development Software &nbsp;which &nbsp;specializing in<br>Forex. Bussiness Marketing &nbsp;and Best Trade Marketing Bussiness development Software</p>

<section>
  <div class="abs feature" style="left:10px">
    <div class="icon gold"><svg width="36" height="30" viewBox="0 0 36 30"><rect x="1" y="7" width="34" height="22" rx="3" fill="#333a40"/><rect x="12" y="2" width="12" height="7" rx="2" fill="none" stroke="#333a40" stroke-width="3"/></svg></div>
    <h3 class="head">Product Features</h3>
    <p>Lorem Ipsum is simply dummy text of the printing and typesetting industry. Lorem Ipsum has been the industry's standard dummy text</p>
    <div class="btn btn-slate btn-small">Read More</div>
  </div>
  <div class="abs feature" style="left:330px">
    <div class="icon"><svg width="34" height="36" viewBox="0 0 34 36"><circle cx="17" cy="13" r="10" fill="#fff"/><circle cx="17" cy="13" r="5" fill="#6f7b86"/><path d="M10 21 L7 34 L13 30 L17 34 L21 30 L27 34 L24 21Z" fill="#fff"/></svg></div>
    <h3 class="head">Documentaion<br>and Demo</h3>
    <p>Lorem Ipsum is simply dummy text of the printing and typesetting industry. Lorem Ipsum has been the industry's standard dummy text</p>
    <div class="btn btn-slate btn-small">Read More</div>
  </div>
  <div class="abs feature" style="left:649px">
    <div class="icon"><svg width="32" height="38" viewBox="0 0 32 38"><path d="M11 2 H21 L18 9 H14Z" fill="#fff"/><circle cx="16" cy="24" r="13" fill="#fff"/><text x="16" y="30" font-size="15" font-family="Arial" font-weight="700" text-anchor="middle" fill="#6f7b86">$</text></svg></div>
    <h3 class="head">Professional<br>Services</h3>
    <p>Lorem Ipsum is simply dummy text of the printing and typesetting industry. Lorem Ipsum has been the industry's standard dummy text</p>
    <div class="btn btn-slate btn-small">Read More</div>
  </div>
  <div class="abs feature" style="left:965px">
    <div class="icon"><svg width="34" height="36" viewBox="0 0 34 36"><circle cx="17" cy="9" r="8" fill="#fff"/><path d="M2 36 Q2 19 17 19 Q32 19 32 36Z" fill="#fff"/><path d="M15 20 L19 20 L18 30 L17 32 L16 30Z" fill="#6f7b86"/></svg></div>
    <h3 class="head">Training</h3>
    <p>Lorem Ipsum is simply dummy text of the printing and typesetting industry. Lorem Ipsum has been the industry's standard dummy text</p>
    <div class="btn btn-slate btn-small">Read More</div>
  </div>
</section>
<div class="abs rule" style="top:1123px;height:1px"></div>
<div class="abs" style="left:594px;top:1119px;width:10px;height:10px;border-radius:50%;background:#eee"></div>

<section>
  <h2 class="abs head sec-title" style="left:12px;top:1157px">Somethings About Our Comapny</h2>
  <div class="abs panel"></div>
  <div class="abs tabs">
    <span class="current">Product</span>
    <span style="left:122px">Product Features</span>
    <span style="left:283px">About Us</span>
  </div>
  <div class="abs product-box" role="img" aria-label="Boxed software package of QuantoMesh"></div>
  <p class="abs panel-copy">Lorem Ipsum is simply dummy text of the printing and typesetting industry. Lorem Ipsum has been the industry's standard dummy text ever since the 1500s, when an unknown printer took a galley of type and scrambled it to make a type specimen book. It has survived not only five centuries, but also the leap into electronic typesetting, remaining essentially unchanged. It was popularised in the 1960s with the release of Typeleaf sheets containing Lorem Ipsum passages, and more recently with desktop publishing software like Folio LayoutMaker including</p>
  <div class="btn btn-slate" style="left:198px;top:1483px;width:106px;height:32px">Get Demo</div>
</section>

<aside>
  <h2 class="abs head sec-title" style="left:780px;top:1157px">Latest News</h2>
  <div class="abs news" style="top:1217px">
    <div class="thumb" role="img" aria-label="Stacked coins against a blue sky" style="background:linear-gradient(#4d7fc4,#9ab7d8)"></div>
    <p>Lorem Ipsum is simply dummy text of the printing and typesetting industry. Lorem Ipsum has been the industry's standard dummy text ever since the</p>
    <em>May 5-2013</em>
  </div>
  <div class="abs news" style="top:1315px">
    <div class="thumb" role="img" aria-label="Rising orange growth bars with an arrow" style="background:linear-gradient(135deg,#fbf6ec,#e9a451)"></div>
    <p>Lorem Ipsum is simply dummy text of the printing and typesetting industry. Lorem Ipsum has been the industry's standard dummy text ever since the</p>
    <em>May 5-2013</em>
  </div>
  <div class="abs news" style="top:1414px">
    <div class="thumb" role="img" aria-label="Business handshake in purple tones" style="background:linear-gradient(135deg,#6a61a8,#c9c6e3)"></div>
    <p>Lorem Ipsum is simply dummy text of the printing and typesetting industry. Lorem Ipsum has been the industry's standard dummy text ever since the</p>
    <em>May 5-2013</em>
  </div>
  <div class="btn btn-gold btn-small" style="left:1090px;top:1513px;width:81px;height:26px;color:var(--white)">See More</div>
</aside>

<section>
  <div class="abs rule" style="top:1584px;height:1px"></div>
  <div class="abs testi-head">
    <h2 class="head">Testimonials</h2>
    <p>You can Judge us by the testimonials of our clients</p>
  </div>
  <svg class="abs arrow" style="left:22px" width="24" height="52" viewBox="0 0 24 52"><polyline points="20,2 4,26 20,50" fill="none" stroke="#c9c9c9" stroke-width="5"/></svg>
  <svg class="abs arrow" style="left:1136px" width="24" height="52" viewBox="0 0 24 52"><polyline points="4,2 20,26 4,50" fill="none" stroke="#c9c9c9" stroke-width="5"/></svg>
  <div class="abs person" style="left:165px">
    <div class="photo" role="img" aria-label="Portrait photo of the client"></div>
    <h4>Mr. Dalen ( CEO of Company Name)</h4>
    <p>Lorem Ipsum is simply dummy text of the printing and typesetting industry. Lorem Ipsum has been the</p>
  </div>
  <div class="abs person" style="left:473px">
    <div class="photo" role="img" aria-label="Portrait photo of the client"></div>
    <h4>Mrs. Oriel ( CEO of Company Name)</h4>
    <p>Lorem Ipsum is simply dummy text of the printing and typesetting industry. Lorem Ipsum has been the</p>
  </div>
  <div class="abs person" style="left:779px">
    <div class="photo" role="img" aria-label="Portrait photo of the client"></div>
    <h4>Mr. Dalen ( CEO of Company Name)</h4>
    <p>Lorem Ipsum is simply dummy text of the printing and typesetting industry. Lorem Ipsum has been the</p>
  </div>
</section>

<footer>
  <div class="abs footer"></div>
  <div class="abs f-col-line" style="left:370px"></div>
  <div class="abs f-col-line" style="left:869px"></div>
  <h3 class="abs f-title" style="left:10px">Quick Links</h3>
  <div class="abs f-links">Privacy Policy<br>Site Map<br>Contact Us</div>
  <p class="abs f-copy">ALL RIGHT ARE RESERVED BY QUANTOMESH.COM</p>

  <h3 class="abs f-title" style="left:466px">Get In Touch With Us</h3>
  <div class="abs social" style="top:2020px"><i></i>Chatterwall</div>
  <div class="abs social" style="top:2070px"><i></i>Orbitline</div>
  <div class="abs social" style="top:2114px"><i></i>Chirpnest</div>
  <p class="abs newsletter">Sign up For Newsletter</p>
  <div class="abs email">ENTER YOUR EMAIL<b>GO</b></div>

  <h3 class="abs f-title" style="left:957px">Contact Us</h3>
  <div class="abs f-logo"><i></i>QuantoMesh</div>
  <div class="abs f-address">4410 Lakeshore Ave<br>Brookfield MI, 48210<br>Call us : 248-555-0190<br>Toll Free : 855-QUANTO MESH</div>
</footer>

</body>
</html>
```